Business Card Design for a Personal Trainer

I need a business card design for my job as a personal trainer. It should have a unique, modern and exclusive design. On the front there should be only my logo with my name and my job. 0163/2918374 Tobias Kellinger Lindenfeldweg 14 80412 Munich Germany The most important contact information is the web adress. it can be bigger than the rest, but its not necessary. The card should be 8,5cmx5,5cm big. Font: Roboto. Colors: black, white, gray, 56c1ff.

```html
<!DOCTYPE html>
<html lang="de">
<head>
<meta charset="utf-8">
<title>Tobias Kellinger – Personal Trainer – Visitenkarte</title>
<link rel="stylesheet" href="https://fonts.googleapis.com/css2?family=Roboto:wght@300;400&family=Roboto+Condensed:wght@300;400&display=swap">
<style>
  :root {
    --stage: #f1f3f5;
    --brand-blue: #66b7ef;
    --band-blue: #56a9e6;
    --card-light: #e6e9ee;
    --ink: #1b1d21;
    --white: #ffffff;
    --photo-dark: #3c3f44;
    --photo-light: #d5d8dd;
  }
  * { margin: 0; padding: 0; box-sizing: border-box; }
  html, body {
    width: 1200px;
    height: 1200px;
    overflow: hidden;
    background: var(--stage);
  }
  .sheet {
    width: 1200px;
    height: 1200px;
    display: flex;
    flex-direction: column;
    align-items: center;
    justify-content: center;
    gap: 56px;
  }
  .card {
    position: relative;
    width: 760px;
    height: 492px;
    overflow: hidden;
    box-shadow: 0 6px 22px rgba(0, 0, 0, 0.12);
  }

  /* Front */
  .card-front {
    background: var(--brand-blue);
    display: flex;
    flex-direction: column;
    align-items: center;
    justify-content: center;
    color: var(--white);
  }
  .brand-name {
    display: flex;
    align-items: center;
    gap: 22px;
    font-family: "Roboto", sans-serif;
    font-weight: 400;
    font-size: 52px;
    letter-spacing: 1px;
    text-transform: uppercase;
  }
  .brand-square {
    width: 34px;
    height: 34px;
    background: var(--white);
  }
  .brand-role {
    display: flex;
    align-items: center;
    gap: 10px;
    margin-top: 6px;
    font-family: "Roboto", sans-serif;
    font-weight: 400;
    font-size: 21px;
    letter-spacing: 7px;
    text-transform: uppercase;
  }
  .brand-role::before,
  .brand-role::after {
    content: "";
    width: 80px;
    height: 2px;
    background: var(--white);
  }

  /* Back */
  .card-back {
    background: var(--card-light);
  }
  .contact-list {
    position: absolute;
    left: 60px;
    top: 100px;
    list-style: none;
    font-family: "Roboto Condensed", sans-serif;
    font-weight: 400;
    font-size: 24px;
    color: var(--ink);
    white-space: nowrap;
  }
  .contact-item {
    display: flex;
    align-items: center;
    gap: 22px;
    height: 62px;
  }
  .contact-icon {
    width: 28px;
    height: 28px;
    flex: none;
    fill: var(--band-blue);
  }
  .web-band {
    position: absolute;
    left: 0;
    right: 0;
    bottom: 0;
    height: 132px;
    background: var(--band-blue);
    display: flex;
    align-items: center;
    padding-left: 80px;
  }
  .web-address {
    font-family: "Roboto Condensed", sans-serif;
    font-weight: 300;
    font-size: 38px;
    color: var(--white);
    white-space: nowrap;
  }
  .portrait {
    position: absolute;
    right: 22px;
    top: 40px;
    width: 216px;
    height: 452px;
    background: linear-gradient(180deg, var(--photo-light) 0%, var(--photo-dark) 45%, #2a2c30 100%);
  }
</style>
</head>
<body>
<main class="sheet">
  <section class="card card-front" aria-label="Visitenkarte Vorderseite">
    <div class="brand-name"><span class="brand-square"></span>Tobias Kellinger</div>
    <div class="brand-role">Personal Trainer</div>
  </section>

  <section class="card card-back" aria-label="Visitenkarte Rückseite">
    <ul class="contact-list">
      <li class="contact-item">
        <svg class="contact-icon" viewBox="0 0 24 24" aria-hidden="true"><path d="M12 1.5a7.5 7.5 0 0 0-7.5 7.5c0 5.6 7.5 13.5 7.5 13.5S19.5 14.6 19.5 9A7.5 7.5 0 0 0 12 1.5zm0 10.5a3 3 0 1 1 0-6 3 3 0 0 1 0 6z"/></svg>
        <span>Lindenfeldweg 14, 80412 München</span>
      </li>
      <li class="contact-item">
        <svg class="contact-icon" viewBox="0 0 24 24" aria-hidden="true"><path d="M6.6 10.8a15.1 15.1 0 0 0 6.6 6.6l2.2-2.2a1 1 0 0 1 1-.25 11.4 11.4 0 0 0 3.6.57 1 1 0 0 1 1 1V20a1 1 0 0 1-1 1A17 17 0 0 1 3 4a1 1 0 0 1 1-1h3.5a1 1 0 0 1 1 1c0 1.250.2 2.45.57 3.57a1 1 0 0 1-.25 1z"/></svg>
        <span>0163/2918374</span>
      </li>
      <li class="contact-item">
        <svg class="contact-icon" viewBox="0 0 24 24" aria-hidden="true"><path d="M2 5h20v14H2zm2 2v.4l8 5.2 8-5.2V7l-8 5.2z"/></svg>
        <span>t.kellinger@postfach-mail.de</span>
      </li>
    </ul>
    <div class="web-band"><span class="web-address">www.tobiaskellinger.de</span></div>
    <div class="portrait" role="img" aria-label="Schwarz-Weiß-Porträt des Trainers mit verschränkten Armen im Sportshirt"></div>
  </section>
</main>
</body>
</html>
```